FLyer for Malaysia's No. 1 Healthcare Job Site (name of job site: Vireta)

Objective of flyer - to get people to register on the job site
Must have:
Logo and Name (Vireta)
Tagline: Malaysia's #1 Healthcare Job site
url: www.vireta-jobs.example
social media links
FB:Vireta
LinkedIn: viretajobs
Instagram: @viretajobs

WE cover the entire healthcare industry areas (doctors, nurses, dentists, pharmacists, psychologists, administrative staff, biomedical engineers....etc)

Please remember that our focus service is our Job-site, we want people to realize in the first look that we are a healthcare Job site.

Flyer size: A5

Color code: #279582 (80%) & #96c836 (20%)

Target Market(s)

All Healthcare Professionals in Malaysia

Industry/Entity Type

Healthcare

Requirements
Must have
• Web site: www.vireta-jobs.example
• Logo and Tagline (attached)
• 2 side design
• Really important (Our Product is our Job site)
Nice to have
• Asian Healthcare professionals, info graphic icons.

```html
<!DOCTYPE html>
<html lang="en">
<head>
<meta charset="utf-8">
<title>Vireta – Healthcare Job Site Flyer</title>
<link rel="stylesheet" href="https://fonts.googleapis.com/css2?family=Passion+One&family=Fira+Sans+Condensed:ital,wght@0,300;0,400;0,500;0,600;1,300&display=swap">
<style>
  :root {
    --teal: #2499a1;
    --green: #9bc93c;
    --grey-band: #e4e6e6;
    --ink: #3d3d3d;
    --ink-soft: #555;
    --paper: #ffffff;
  }
  * { margin: 0; padding: 0; box-sizing: border-box; }
  html, body { width: 886px; height: 1200px; overflow: hidden; background: var(--paper); }
  .flyer {
    position: relative; width: 886px; height: 1200px; overflow: hidden;
    background: var(--paper);
    font-family: "Fira Sans Condensed", "Arial Narrow", sans-serif;
  }
  .backdrop { position: absolute; inset: 0; width: 886px; height: 1200px; }

  .brand { position: absolute; left: 44px; top: 78px; display: flex; align-items: center; gap: 16px; }
  .brand-dot { width: 40px; height: 40px; border-radius: 50%; background: var(--teal); }
  .brand-name {
    font-size: 76px; font-weight: 500; line-height: 1;
    color: var(--teal); letter-spacing: 1px;
  }

  .tagline {
    position: absolute; right: 338px; top: 178px;
    text-align: right; color: var(--teal);
    font-size: 44px; font-weight: 400; line-height: 52px;
  }

  .hiring-tab { position: absolute; left: 576px; top: 50px; width: 244px; height: 165px; background: #d5d8d8; border-radius: 4px; }
  .hiring-badge {
    position: absolute; left: 586px; top: 58px; width: 246px; height: 157px;
    background: var(--green); border: 6px solid var(--paper);
    display: flex; flex-direction: column; align-items: center; justify-content: center;
    font-family: "Passion One", sans-serif; color: var(--paper);
    font-size: 72px; line-height: 60px; letter-spacing: 2px;
  }

  .steps { position: absolute; left: 34px; top: 380px; list-style: none; }
  .step { display: grid; grid-template-columns: 34px auto; margin-bottom: 18px; }
  .step-icon { width: 22px; height: 22px; margin-top: 10px; }
  .step-title { font-size: 32px; font-weight: 600; color: var(--ink); line-height: 38px; }
  .step-text { grid-column: 2; font-size: 21px; font-weight: 300; color: var(--ink-soft); line-height: 25px; }

  .journey { position: absolute; left: 27px; top: 670px; width: 400px; }
  .journey-title { font-size: 31px; font-weight: 600; color: var(--teal); letter-spacing: -0.2px; margin-bottom: 12px; }
  .journey-text { font-size: 20.5px; font-weight: 300; color: var(--ink-soft); line-height: 24px; }
  .journey-text .highlight { color: var(--teal); font-weight: 400; }

  .doctor-photo {
    position: absolute; left: 450px; top: 340px; width: 436px; height: 765px;
    border-radius: 210px 210px 0 0;
    background: radial-gradient(ellipse at 55% 45%, #fbfcfc 0%, #eef1f2 55%, rgba(230,236,238,0.85) 80%, rgba(36,153,161,0) 100%);
  }

  .social { position: absolute; left: 43px; top: 905px; color: var(--paper); }
  .social-intro { font-style: italic; font-weight: 300; font-size: 23px; line-height: 28px; margin-bottom: 12px; }
  .social-list { list-style: none; }
  .social-item { display: flex; align-items: center; gap: 12px; font-size: 23px; font-weight: 300; height: 36px; margin-left: 7px; }
  .social-dot { width: 26px; height: 26px; border-radius: 50%; background: var(--paper); }

  .contact-bar {
    position: absolute; left: 43px; top: 1097px; width: 806px; height: 73px;
    background: var(--paper); border: 1.5px dashed #9a9a9a; border-radius: 14px;
    box-shadow: 0 2px 6px rgba(0,0,0,0.18);
    display: flex; align-items: center; padding-left: 38px; gap: 16px;
  }
  .contact-label { font-size: 22px; font-weight: 600; color: var(--teal); }
  .contact-url { display: flex; align-items: center; gap: 8px; font-size: 31px; font-weight: 600; color: var(--green); }
</style>
</head>
<body>
<main class="flyer">
  <svg class="backdrop" viewBox="0 0 700 992" preserveAspectRatio="none" aria-hidden="true">
    <path fill="var(--grey-band)" d="M490,0 L535,0 C560,120 530,220 500,300 C470,380 430,470 400,560 C365,650 372,720 360,800 C345,880 352,950 355,992 L330,992 C320,900 318,820 328,740 C338,640 358,560 388,470 C418,380 458,300 478,210 C493,140 500,60 490,0 Z"/>
    <path fill="var(--teal)" d="M535,0 L700,0 L700,992 L355,992 C352,950 345,880 360,800 C372,720 365,650 400,560 C430,470 470,380 500,300 C530,220 560,120 535,0 Z"/>
    <path fill="var(--grey-band)" d="M0,690 C160,680 300,730 350,870 C362,910 365,950 368,992 L0,992 Z"/>
    <path fill="var(--green)" d="M0,705 C150,695 280,740 330,860 C345,900 350,950 355,992 L0,992 Z"/>
  </svg>

  <div class="doctor-photo" role="img" aria-label="Photo of a smiling female doctor in a white coat with a stethoscope, arms crossed"></div>

  <header class="brand">
    <span class="brand-dot"></span>
    <span class="brand-name">Vireta</span>
  </header>

  <p class="tagline">healthcare<br>Malaysia's #1 job site</p>

  <div class="hiring-tab"></div>
  <div class="hiring-badge"><span>NOW</span><span>HIRING</span></div>

  <ol class="steps">
    <li class="step">
      <svg class="step-icon" viewBox="0 0 22 22" aria-hidden="true"><circle cx="11" cy="11" r="11" fill="#2d4d55"/><path d="M9,6 L14,11 L9,16" stroke="#fff" stroke-width="2.6" fill="none"/></svg>
      <span class="step-title">Create Profile</span>
      <span class="step-text">It's EASY – Create A Profile Within Minutes</span>
    </li>
    <li class="step">
      <svg class="step-icon" viewBox="0 0 22 22" aria-hidden="true"><circle cx="11" cy="11" r="11" fill="#2d4d55"/><path d="M9,6 L14,11 L9,16" stroke="#fff" stroke-width="2.6" fill="none"/></svg>
      <span class="step-title">Search Jobs</span>
      <span class="step-text">Check Out Healthcare Opportunities By<br>Top Employers</span>
    </li>
    <li class="step">
      <svg class="step-icon" viewBox="0 0 22 22" aria-hidden="true"><circle cx="11" cy="11" r="11" fill="#2d4d55"/><path d="M9,6 L14,11 L9,16" stroke="#fff" stroke-width="2.6" fill="none"/></svg>
      <span class="step-title">Apply!</span>
      <span class="step-text">Grow Your CAREER!</span>
    </li>
  </ol>

  <section class="journey">
    <h2 class="journey-title">BEGIN YOUR JOURNEY NOW</h2>
    <p class="journey-text">We are <span class="highlight">Malaysia's #1 Healthcare Job Site</span><br>fully dedicated to the healthcare industry,<br>being a part of the new generation of Job<br>Sites worldwide.</p>
  </section>

  <section class="social">
    <p class="social-intro">We look forward to<br>hearing from you!!</p>
    <ul class="social-list">
      <li class="social-item"><span class="social-dot"></span>vireta</li>
      <li class="social-item"><span class="social-dot"></span>viretajobs</li>
      <li class="social-item"><span class="social-dot"></span>@viretajobs</li>
    </ul>
  </section>

  <footer class="contact-bar">
    <span class="contact-label">For more information contact us at</span>
    <span class="contact-url">
      <svg width="30" height="30" viewBox="0 0 30 30" aria-hidden="true">
        <circle cx="15" cy="15" r="12.5" fill="none" stroke="var(--green)" stroke-width="2.5"/>
        <ellipse cx="15" cy="15" rx="5.5" ry="12.5" fill="none" stroke="var(--green)" stroke-width="2"/>
        <path d="M3,15 H27 M5,9 H25 M5,21 H25" stroke="var(--green)" stroke-width="2"/>
      </svg>
      www.vireta-jobs.example
    </span>
  </footer>
</main>
</body>
</html>
```